Strong, Clean Book Design Needed for "The Lantern Keeper"

I need a strong, clean, masculine cover of a book that focuses on helping men restore honor to what it means to be a good husband. (I also need a back cover and spine done as well). I would like the cover to be either a white, red, or black cover. I have attached 3 books that I would like to use as examples to model after. I also attached a word document to show the potential layouts I would like to see and how that parallel the example covers.

Specs:
- Book is 150 pages long
- Size is 5.25 x 8

Target Market(s)

Christian men who are married or looking to be married.

Font styles to use
Serif
Sans Serif

Colors
ec1f27
f04a50
ffffff
000000
1b1b1b
757575

Requirements
Must have
• - A design that resembles/has a similar feel to one of the three examples that are attached and laid out similarly to one of the 3 designs in the word doc "3 Book Designs"
• - These elements on the front cover: Title: The Lantern Keeper, Subtitle: Restoring the honor of a Christ-centered marriage, Author Name: Dale Forsby
• - A strong design that is simple yet creative.
• - Strong masculine font that is bold but not too flashy
• - Red should be included either as the title font color or as the overall cover color.
• - The back of the book should have the attached file "Back of the book" text on the back
Nice to have
• - A color contrast, like a strip of another color (see "example 3" attached file) across the front for the subtitle or the author name.
• - Including the attached sword file as a somewhat transparent image on the cover, but absolutely not necessary.
• - If there is going to be any highlighting of words in the subtitle, they should be the word "honor" and "Christ-centered"
Should not have
• Any religious symbols, such as a cross.

```html
<!DOCTYPE html>
<html lang="en">
<head>
<meta charset="utf-8">
<title>The Lantern Keeper – Book Covers</title>
<link rel="stylesheet" href="https://fonts.googleapis.com/css2?family=Anton&family=Cinzel:wght@400;700&family=Oswald:wght@600;700&family=Open+Sans:ital,wght@0,600;0,700;1,700&display=swap">
<style>
  :root {
    --red: #ec1f27;
    --red-deep: #a5121a;
    --red-dark: #7e0c12;
    --red-soft: #f04a50;
    --white: #ffffff;
    --black: #000000;
    --ink: #1b1b1b;
    --grey: #757575;
    --cream: #f3e6cf;
    --stage: #ececec;
  }
  * { margin: 0; padding: 0; box-sizing: border-box; }
  html, body { width: 1200px; height: 1000px; overflow: hidden; background: var(--stage); }
  .canvas { position: relative; width: 1200px; height: 1000px; }

  /* Back cover */
  .back-cover {
    position: absolute; left: 110px; top: 150px; width: 470px; height: 700px;
    background: radial-gradient(ellipse at 40% 35%, var(--red) 0%, var(--red-deep) 60%, var(--red-dark) 100%);
    padding: 42px 34px 0 34px; color: var(--white);
    box-shadow: 0 10px 30px rgba(0,0,0,.25);
  }
  .back-heading {
    font-family: "Oswald", sans-serif; font-weight: 700; color: var(--cream);
    font-size: 31px; line-height: 1.02; text-transform: uppercase; letter-spacing: .5px;
    margin-bottom: 18px;
  }
  .back-heading span { display: block; }
  .back-heading .indent { padding-left: 14px; }
  .back-copy p {
    font-family: "Open Sans", sans-serif; font-weight: 600; font-size: 10.2px; line-height: 1.5;
    text-align: justify; margin-bottom: 11px;
  }
  .back-copy em { font-style: italic; font-weight: 700; }
  .back-sword {
    display: block; width: 300px; height: 14px; margin: 4px 0 16px 110px;
    background: linear-gradient(90deg, rgba(0,0,0,0), rgba(60,0,4,.55) 40%, rgba(30,0,2,.8));
    border-radius: 7px;
  }
  .author-bio {
    font-family: "Open Sans", sans-serif; font-weight: 600; font-size: 10.5px; line-height: 1.5;
    text-align: justify;
  }
  .author-bio strong { font-weight: 700; text-transform: uppercase; }

  /* Front cover */
  .front-cover {
    position: absolute; left: 615px; top: 150px; width: 470px; height: 700px;
    background: var(--white); overflow: hidden;
    box-shadow: 0 10px 30px rgba(0,0,0,.25);
  }
  .title {
    position: absolute; left: 26px; top: 50px; width: 340px;
    font-family: "Anton", sans-serif; font-weight: 400; color: var(--red); text-transform: uppercase;
    line-height: .92;
  }
  .title span { display: block; transform-origin: left center; white-space: nowrap; }
  .title .the { font-size: 92px; padding-left: 110px; letter-spacing: 2px; transform: scaleX(.8); }
  .title .word { font-size: 120px; letter-spacing: 0; transform: scaleX(.78); }
  .subtitle {
    position: absolute; left: 0; width: 380px; top: 442px; text-align: center;
    font-family: "Cinzel", serif; font-weight: 400; color: var(--ink);
    font-size: 17px; line-height: 1.3; letter-spacing: .3px;
  }
  .subtitle b { font-weight: 700; }
  .author-band { position: absolute; left: 0; top: 500px; width: 470px; height: 110px; }
  .author-name {
    position: absolute; left: 0; width: 380px; top: 531px; text-align: center;
    font-family: "Cinzel", serif; font-weight: 400; color: var(--white);
    font-size: 38px; letter-spacing: 1px; white-space: nowrap;
  }
  .sword-art {
    position: absolute; left: 382px; top: 0; width: 62px; height: 700px;
    background: linear-gradient(180deg, #efe8da 0%, #d9ceb8 38%, #8a5a3a 47%, #1d1a1c 52%, #0c0c0e 100%);
  }
</style>
</head>
<body>
<main class="canvas">

  <section class="back-cover" aria-label="Back cover">
    <h2 class="back-heading">
      <span>Do you have</span>
      <span>what it takes to be</span>
      <span class="indent">a Lantern Keeper?</span>
    </h2>
    <div class="back-copy">
      <p>The samurai were fearsome Japanese warriors known for their discipline, loyalty, and strict adherence to their code of honor, bushido. Along with their ferocity on the battlefield, they also embodied the heart and sacrifice of “those who serve,” the meaning of the word samurai. The samurai lived, and more importantly, died by the honor that characterized these ideals. The samurai way of life transformed the nation, culture, and moral code of Japan, and continues to do so to this day…</p>
      <p>The Lantern Keeper is more than just an interesting read: it is a radically Christ-centered approach to marriage. Dale Forsby recaptures what it means to be a man and an effective leader in a marriage by simply, but powerfully, laying out the Biblical qualities found in Ephesians 5 that God calls husbands to embody. With a fresh and unique perspective, Dale parallels how samurai warriors once lived and how godly husbands should live in a way that restores and highlights the honor, sacrifice, and purpose of marriage. This book will undoubtedly shift the way men view and function in their role as a husband and gives them practical nuts and bolts suggestions for day-to-day success as a husband.</p>
      <p>This is a wake-up call to all husbands everywhere: be the man and the husband God has called you to be. Although it is not easy, it is guaranteed to transform your life… and your marriage!</p>
      <p>Embrace the call of a truly Christ-centered marriage.<br><em>Embrace the way of the Lantern Keeper.</em></p>
    </div>
    <span class="back-sword" role="img" aria-label="Faint illustration of a sword lying horizontally"></span>
    <p class="author-bio"><strong>Dale Forsby</strong> is the Microchurch Pastor at the Cedar Hall in Millbrook, Oregon where he has a heart for marriage and multiplying disciples and churches. He has a fierce love for Jesus and has been married to his wife, Joanna, for over a decade. They have two beautiful daughters, Miriam and Elise.</p>
  </section>

  <section class="front-cover" aria-label="Front cover">
    <h1 class="title">
      <span class="the">The</span>
      <span class="word">Lantern</span>
      <span class="word">Keeper</span>
    </h1>
    <p class="subtitle">Restoring the <b>Honor</b> of a<br><b>Christ-Centered</b> Marriage</p>
    <svg class="author-band" viewBox="0 0 470 110" preserveAspectRatio="none" aria-hidden="true">
      <polygon fill="var(--red)" points="0,12 18,6 34,14 52,4 70,10 92,2 110,12 128,6 150,14 172,3 196,10 218,5 240,13 262,4 286,11 308,2 330,12 352,6 376,14 398,4 420,10 444,3 470,9 470,100 448,106 426,98 404,108 380,100 356,107 332,99 310,108 286,101 262,106 240,98 216,108 194,100 170,106 146,98 124,108 100,101 78,107 56,99 34,108 16,100 0,106"/>
    </svg>
    <p class="author-name">Dale Forsby</p>
    <div class="sword-art" role="img" aria-label="Vertical katana with carved ivory handle and ornate guard running down the right edge"></div>
  </section>

</main>
</body>
</html>
```